New Gay dating app for meeting new people

I am looking for someone to design me a new gay dating app. It should have features such as a sign in page, being able to upload pictures, make a profile, and be able to know the distance from someone and be able to send a location.

Could you please provide the finished product CODED and ready for use.

The colours are up to the designer.

The name of the app LumaVox

If you need to ask me any questions don't hesitate to ask me for anything.

Target Market(s)

Gay males 18+ years old

Industry/Entity Type

Dating

Requirements
Must have
• Be able to chat

```html
<!DOCTYPE html>
<html lang="en">
<head>
<meta charset="utf-8">
<title>LumaVox – Chat</title>
<link href="https://fonts.googleapis.com/css2?family=Open+Sans:wght@300;400;600&display=swap" rel="stylesheet">
<style>
  :root{
    --bar-dark:#2e2e2e;
    --screen:#585858;
    --composer:#3c3c3c;
    --bubble-in:#8f8f8f;
    --bubble-out:#ffffff;
    --text-light:#f2f2f2;
    --text-dark:#4a4a4a;
    --meta:#e4e4e4;
    --avatar-ring:#ffffff;
  }
  *{box-sizing:border-box;margin:0;padding:0}
  html,body{width:677px;height:1200px;overflow:hidden;background:var(--screen)}
  body{font-family:"Open Sans",Arial,sans-serif;color:var(--text-light)}
  .screen{position:relative;width:677px;height:1200px;background:var(--screen)}

  .status-bar{position:absolute;top:0;left:0;width:100%;height:44px;background:var(--bar-dark);
    display:flex;align-items:center;justify-content:space-between;padding:0 14px;font-size:22px;color:#fff}
  .status-left,.status-right{display:flex;align-items:center;gap:8px;width:220px}
  .status-right{justify-content:flex-end}
  .status-time{font-weight:400}

  .nav-bar{position:absolute;top:44px;left:0;width:100%;height:154px;background:var(--bar-dark);
    display:flex;align-items:center;justify-content:center}
  .nav-title{font-size:34px;font-weight:300;color:#fff;margin-top:-44px}
  .nav-menu{position:absolute;left:52px;top:48px}
  .nav-settings{position:absolute;right:38px;top:42px}

  .avatar{position:absolute;width:110px;height:110px;border-radius:50%;border:5px solid var(--avatar-ring);
    background:radial-gradient(circle at 50% 40%,#c79a78 0%,#8a6246 45%,#3f6f87 100%)}
  .avatar--bare{background:radial-gradient(circle at 50% 40%,#d6a98a 0%,#9c6e52 50%,#e9e9e9 100%)}

  .bubble{position:absolute;font-size:15.5px;line-height:28px;padding:14px 18px}
  .bubble--in{background:var(--bubble-in);color:var(--text-light)}
  .bubble--in::before{content:"";position:absolute;left:-16px;top:24px;border:10px solid transparent;
    border-right:16px solid var(--bubble-in);border-left:0}
  .bubble--out{background:var(--bubble-out);color:var(--text-dark);display:flex;align-items:center}
  .bubble--out::after{content:"";position:absolute;right:-16px;top:24px;border:10px solid transparent;
    border-left:16px solid var(--bubble-out);border-right:0}

  .meta{position:absolute;display:flex;align-items:center;gap:8px;font-size:10px;color:var(--meta)}

  .composer{position:absolute;left:0;bottom:0;width:100%;height:94px;background:var(--composer);
    display:flex;align-items:center;justify-content:center;font-size:26px;font-weight:300;color:#eee}
</style>
</head>
<body>
<main class="screen">
  <header class="status-bar">
    <div class="status-left">
      <svg width="54" height="12" viewBox="0 0 54 12"><g fill="#fff"><circle cx="5" cy="6" r="4.5"/><circle cx="16" cy="6" r="4.5"/><circle cx="27" cy="6" r="4.5"/></g><g fill="none" stroke="#fff" stroke-width="1.2"><circle cx="38" cy="6" r="4"/><circle cx="49" cy="6" r="4"/></g></svg>
      <span>QUELLNET</span>
      <svg width="22" height="16" viewBox="0 0 22 16"><g fill="none" stroke="#fff" stroke-width="2.2" stroke-linecap="round"><path d="M2 6a13 13 0 0 1 18 0"/><path d="M5.5 9.5a8 8 0 0 1 11 0"/></g><circle cx="11" cy="13.5" r="2" fill="#fff"/></svg>
    </div>
    <span class="status-time">2:40 PM</span>
    <div class="status-right">
      <svg width="12" height="20" viewBox="0 0 12 20"><path d="M1 5l10 9-5 4V2l5 4-10 9" fill="none" stroke="#fff" stroke-width="1.6"/></svg>
      <span>43%</span>
      <svg width="44" height="20" viewBox="0 0 44 20"><rect x="1" y="1" width="38" height="18" rx="3" fill="none" stroke="#fff" stroke-width="1.6"/><rect x="4" y="4" width="15" height="12" fill="#fff"/><rect x="40" y="7" width="3" height="6" fill="#fff"/></svg>
    </div>
  </header>

  <nav class="nav-bar">
    <svg class="nav-menu" width="32" height="26" viewBox="0 0 32 26"><g fill="#fff"><rect y="0" width="32" height="4" rx="1"/><rect y="11" width="32" height="4" rx="1"/><rect y="22" width="32" height="4" rx="1"/></g></svg>
    <h1 class="nav-title">Chat</h1>
    <svg class="nav-settings" width="44" height="40" viewBox="0 0 44 40">
      <g fill="#fff">
        <circle cx="16" cy="22" r="10"/>
        <g transform="translate(16 22)"><rect x="-3" y="-15" width="6" height="30"/><rect x="-15" y="-3" width="30" height="6"/><rect x="-3" y="-15" width="6" height="30" transform="rotate(45)"/><rect x="-3" y="-15" width="6" height="30" transform="rotate(-45)"/></g>
        <circle cx="34" cy="10" r="6"/>
        <g transform="translate(34 10)"><rect x="-2" y="-9" width="4" height="18"/><rect x="-9" y="-2" width="18" height="4"/><rect x="-2" y="-9" width="4" height="18" transform="rotate(45)"/><rect x="-2" y="-9" width="4" height="18" transform="rotate(-45)"/></g>
      </g>
      <circle cx="16" cy="22" r="4" fill="#2e2e2e"/><circle cx="34" cy="10" r="2.5" fill="#2e2e2e"/>
    </svg>
  </nav>

  <section class="conversation">
    <div class="avatar" style="left:65px;top:261px" role="img" aria-label="Profile photo of the match"></div>
    <p class="bubble bubble--in" style="left:221px;top:275px;width:348px;height:167px">Lorem ipsum dolor sit amet, consectetur adipiscing elit. Maecenas suscipit blandit eros sed vulputate. Sed mollis commo&shy;do elit vitae mollis.</p>
    <div class="meta" style="right:110px;top:456px"><svg width="16" height="12" viewBox="0 0 16 12"><path d="M1 6l5 5 9-10" fill="none" stroke="#e4e4e4" stroke-width="2"/></svg>11:00 PM</div>

    <p class="bubble bubble--out" style="left:61px;top:548px;width:345px;height:66px">Sed mollis commodo elit vitae mollis.</p>
    <div class="avatar avatar--bare" style="left:457px;top:527px" role="img" aria-label="Profile photo of the user"></div>
    <div class="meta" style="left:79px;top:634px"><svg width="16" height="12" viewBox="0 0 16 12"><path d="M1 6l5 5 9-10" fill="none" stroke="#e4e4e4" stroke-width="2"/></svg>11:00 PM</div>

    <div class="avatar" style="left:65px;top:701px" role="img" aria-label="Profile photo of the match"></div>
    <p class="bubble bubble--in" style="left:221px;top:715px;width:348px;height:167px">Lorem ipsum dolor sit amet, consectetur adipiscing elit. Maecenas suscipit blandit eros sed vulputate. Sed mollis commo&shy;do elit vitae mollis.</p>
    <div class="meta" style="right:110px;top:894px"><svg width="16" height="12" viewBox="0 0 16 12"><path d="M1 6l5 5 9-10" fill="none" stroke="#e4e4e4" stroke-width="2"/></svg>11:00 PM</div>
  </section>

  <footer class="composer">Type here</footer>
</main>
</body>
</html>
```